The maple crew

I want it as prefession and attractive as possible we are a lawnmowing business

Phone number 605-318-2264
Name- Carlos Whitfield
Email- themaplecrewsd@fernpost.com

```html
<!DOCTYPE html>
<html lang="en">
<head>
<meta charset="utf-8">
<title>The Maple Crew – Business Card</title>
<link href="https://fonts.googleapis.com/css2?family=Bree+Serif&family=Oswald:wght@500;700&family=Poppins:wght@600&display=swap" rel="stylesheet">
<style>
  :root {
    --backdrop: #002a10;
    --card-white: #ffffff;
    --lawn: #66bc46;
    --lawn-light: #b6d66c;
    --forest: #0d5e3a;
    --ink: #00300f;
  }
  * { margin: 0; padding: 0; box-sizing: border-box; }
  html, body {
    width: 1200px; height: 1200px; overflow: hidden;
    background: var(--backdrop);
  }
  .stage { position: relative; width: 1200px; height: 1200px; }

  .card { position: absolute; left: 334px; width: 587px; height: 358px; overflow: hidden; }
  .card--front {
    top: 250px; background: var(--card-white);
    box-shadow: 6px 8px 14px rgba(0,0,0,.35);
  }
  .card--back { top: 682px; height: 356px; background: var(--lawn); }

  .holder-name {
    position: absolute; left: 34px; top: 44px;
    font-family: "Bree Serif", serif; font-size: 42px;
    color: var(--ink); letter-spacing: 0.5px;
  }
  .lawn-scene {
    position: absolute; left: 0; top: 87px; width: 587px; height: 154px;
    background: linear-gradient(to bottom, rgba(182,214,108,0) 0%, rgba(182,214,108,.55) 55%, var(--lawn) 100%);
  }
  .lawn-band { position: absolute; left: 0; top: 241px; width: 587px; height: 42px; background: var(--lawn); }
  .contact-bar { position: absolute; left: 0; top: 283px; width: 587px; height: 48px; background: var(--lawn-light); }
  .contact-bar svg.slant { position: absolute; left: 0; top: 0; }
  .contact { position: absolute; top: 0; height: 48px; display: flex; align-items: center; gap: 9px; }
  .contact--phone { left: 40px; color: #fff; font-family: "Oswald", sans-serif; font-weight: 500; font-size: 24px; letter-spacing: .3px; }
  .contact--email { left: 246px; color: var(--ink); font-family: "Poppins", sans-serif; font-weight: 600; font-size: 14.5px; letter-spacing: .6px; }
  .footer-band { position: absolute; left: 0; top: 331px; width: 587px; height: 27px; background: var(--lawn); }

  .crew-name {
    position: absolute; inset: 0; display: flex; align-items: center; justify-content: center;
    font-family: "Oswald", sans-serif; font-weight: 700; font-size: 62px;
    text-transform: uppercase; color: var(--forest); letter-spacing: 1px;
  }
</style>
</head>
<body>
<main class="stage">
  <section class="card card--front">
    <h1 class="holder-name">Carlos Whitfield</h1>
    <div class="lawn-scene" role="img" aria-label="Illustration of tall grass blades and a person pushing a lawn mower"></div>
    <div class="lawn-band"></div>
    <div class="contact-bar">
      <svg class="slant" width="232" height="48" viewBox="0 0 232 48"><polygon points="0,0 200,0 232,48 0,48" fill="var(--ink)"/></svg>
      <div class="contact contact--phone">
        <svg width="20" height="20" viewBox="0 0 24 24"><path d="M6.6 10.8a15.1 15.1 0 0 0 6.6 6.6l2.2-2.2c.3-.3.7-.4 1-.2 1.1.4 2.3.6 3.6.6.6 0 1 .4 1 1V20c0 .6-.4 1-1 1A17 17 0 0 1 3 4c0-.6.4-1 1-1h3.5c.6 0 1 .4 1 1 0 1.3.2 2.5.6 3.6.1.3 0 .7-.2 1z" fill="#fff"/></svg>
        <span>605-318-2264</span>
      </div>
      <div class="contact contact--email">
        <svg width="25" height="16" viewBox="0 0 25 16"><rect x="1" y="1" width="23" height="14" fill="none" stroke="var(--ink)" stroke-width="1.8"/><path d="M1 1l11.5 8L24 1M1 15l8-7M24 15l-8-7" fill="none" stroke="var(--ink)" stroke-width="1.6"/></svg>
        <span>themaplecrewsd@fernpost.com</span>
      </div>
    </div>
    <div class="footer-band"></div>
  </section>

  <section class="card card--back">
    <div class="crew-name">The Maple Crew</div>
  </section>
</main>
</body>
</html>
```